"The Craft of Patron Care," fourth edition cover design

Later this year, my publisher, Harold Penmarsh & Daughters, will issue a fourth, substantially revised edition of "The Craft of Patron Care," following the 2016 publication of the third edition and the second and first versions that were issued earlier.

To distinguish this new edition from previous ones, I need a cover design that visually connects and is consistent with what has preceded it, while signaling this is a new and different, worthy of prospective readers/buyers’ attention.

Attached are three different verbal approaches to the new cover; these are NOT MEANT to serve as actual designs, but rather will give you a sense of how language is to be deployed:

The first emphasizes “ART” as the key visual word in the book title;
The second emphasizes “CLIENT SERVICE” as the key visual words in the book title; and,
The third emphasizes just the word "CLIENT" in the book title.

A top-of-the-page is a pre-head that applies to all three versions:
“6 TIMELESS PRINCIPLES FOR ADVERTISING & MARKETING PRO’s
IN AN AI WORLD"

There's a mid-page sub-head for all three versions:
“THE CLASSIC GUIDE,” followed by
“FOURTH EDITION BY GERALD ASHCOMBE

And there's a one-line, bottom-of-the-page designation:
“Foreword by Mae Dunford, Global Executive Creative Director, Starbolt"

The pallette for the previously published third edition was black with red as an accent color on a field of white; I've attached a sample for reference, so you can see how it was executed. For this new fourth edition, I'd like to change the accent color from red to either Wedgewood blue, or British racing green, or an alternative that is assertive and color saturated -- think of primary colors -- that contrast sufficiently with the base of black. As an alternative, you can consider a cover that used either Wedgewood blue, British racing green, or another possibility as a full-bleed field, with copy content either revered out or surprinted.

Lastly, while the new cover largely is meant to be typographically driven, if you can come up with a visual metaphor that illustrates and builds on the book's title, that would be very helpful. By way of reference, the third edition's book cover attempted to do this by introducing a visual element at the end of the book's title that's meant to represent an artist's paint splatter (although I admit it didn't work as well as it should).

Target Market(s)

Prospective purchasers of the book who might discover copies at a bookstore, but more likely will encounter it through online distributors such as Riverdex, Hartwell & Pike, and Tindall’s.

Industry/Entity Type

Advertising and marketing

Font styles to use
Serif
Sans Serif
Other font styles liked:
• A mix of serif and san-serif typefaces is okay. for the examples I shared, I relieid on "Arial Rounded Bold" but you need not be weeded to this. If you opt to mix in a serif font, I am partial to Cambria as a typeface.

Requirements
Must have
• To achieve the goal of being “connected with but distinct” from previous editions, the new cover should be:  Largely typographic, but displaying a color palette different from the previous editions’ black-plus-red-accent on a canvas of white.  Any new accent color selected for use should be vibrant, strong, and highly saturated; think “British racing green,” “Wedgewood blue,” or their equivalents.  In addition to a powerful, “billboard” approach to type and color, consider other visual metaphors that are likely to engage the readers. The winning cover design will stand out from other books, while connecting with the previously published third edition.
Nice to have
• If you can find way to illustrate the book's title through a visual metaphor, that would be ideal.a
Should not have
• Anything that is frivolous or non-sensical

```html
<!DOCTYPE html>
<html lang="en">
<head>
<meta charset="utf-8">
<title>The Craft of Patron Care — Fourth Edition</title>
<link rel="stylesheet" href="https://fonts.googleapis.com/css2?family=Public+Sans:wght@600;700;800&display=swap">
<style>
  :root {
    --ink: #0b0b0b;
    --accent: #7a9fcb;
    --paper: #ffffff;
    --mist: #dcebf6;
    --mist-deep: #c7dff0;
  }
  html, body {
    margin: 0;
    padding: 0;
    width: 800px;
    height: 1200px;
    overflow: hidden;
    background: var(--paper);
  }
  .cover {
    position: relative;
    width: 800px;
    height: 1200px;
    background: var(--paper);
    font-family: "Public Sans", Arial, sans-serif;
    color: var(--ink);
    overflow: hidden;
  }
  .prehead {
    position: absolute;
    top: 78px;
    left: 0;
    width: 800px;
    margin: 0;
    text-align: center;
    font-weight: 700;
    font-size: 31px;
    line-height: 40px;
    letter-spacing: 0.6px;
  }
  .accent { color: var(--accent); }
  .title-lockup {
    position: absolute;
    top: 0;
    left: 0;
    width: 800px;
    height: 600px;
  }
  .title-lockup text {
    font-family: "Public Sans", Arial, sans-serif;
  }
  .title-the, .title-of, .title-patron { fill: var(--ink); font-weight: 800; }
  .title-craft { fill: var(--accent); font-weight: 800; }
  .edition {
    position: absolute;
    top: 632px;
    left: 0;
    width: 800px;
    text-align: center;
    margin: 0;
  }
  .edition-guide {
    display: block;
    font-weight: 700;
    font-size: 32px;
    line-height: 40px;
    letter-spacing: 0.8px;
  }
  .edition-number {
    display: block;
    margin-top: 3px;
    color: var(--accent);
    font-weight: 700;
    font-size: 40px;
    line-height: 48px;
    letter-spacing: 0.4px;
  }
  .metaphor-art {
    position: absolute;
    left: 236px;
    top: 770px;
    width: 330px;
    height: 205px;
    border-radius: 48% 52% 46% 54% / 55% 50% 50% 45%;
    background: radial-gradient(ellipse at 55% 50%, var(--mist-deep) 0%, var(--mist) 55%, rgba(220,235,246,0) 100%);
  }
  .byline {
    position: absolute;
    top: 1046px;
    left: 0;
    width: 800px;
    margin: 0;
    text-align: center;
    color: var(--accent);
    font-weight: 700;
    font-size: 31px;
    line-height: 38px;
    letter-spacing: 0.8px;
  }
  .foreword {
    position: absolute;
    top: 1106px;
    left: 0;
    width: 800px;
    margin: 0;
    text-align: center;
    font-weight: 700;
    font-size: 19px;
    line-height: 28px;
    letter-spacing: 0.9px;
  }
</style>
</head>
<body>
  <main class="cover">
    <p class="prehead">
      <span class="accent">6 TIMELESS PRINCIPLES</span> FOR ADVERTISING<br>
      &amp; MARKETING PRO’s IN AN <span class="accent">AI WORLD</span>
    </p>

    <svg class="title-lockup" viewBox="0 0 800 600" aria-label="The Craft of Patron Care">
      <text class="title-the" x="194" y="270" font-size="53" textLength="89" lengthAdjust="spacingAndGlyphs">THE</text>
      <text class="title-craft" x="156" y="492" font-size="276" textLength="487" lengthAdjust="spacingAndGlyphs">CRAFT</text>
      <text class="title-of" x="156" y="548" font-size="31" textLength="38" lengthAdjust="spacingAndGlyphs">OF</text>
      <text class="title-patron" x="213" y="557" font-size="55" textLength="385" lengthAdjust="spacing">PATRON CARE</text>
    </svg>

    <p class="edition">
      <span class="edition-guide">THE CLASSIC GUIDE</span>
      <span class="edition-number">FOURTH EDITION</span>
    </p>

    <div class="metaphor-art" role="img" aria-label="Soft pale-blue paint blobs with two deep green dots, suggesting an artist's palette"></div>

    <p class="byline">BY GERALD ASHCOMBE</p>

    <p class="foreword">Foreword by Mae Dunford, Global Executive Creative Director, Starbolt</p>
  </main>
</body>
</html>
```